Mobile technology Business Card Design Project

We need a business card design for our company based in Sydeny Australia, that takes a company's desktop sites and creates a mobile site compatible to all mobile/smartphone devices. This allows greater ease of use and generally faster business conversion than customers using a desktop site.
Our company is called VelqCore but we refer to it as Velq Corestreams. If this could be represented somewhere on the business card that would be great.
Am open to suggestions regarding the colours but a high tech  theme would be good.
Happy bidding!

Target Market(s)
Business owner that has a website and is reasonably savvy regarding online/mobile marketing.
Industry/Entity Type
Business
Requirements
Must have
- Business card details:
Director Peter Langwade
Address: 5/41 Dunmore rd, Kelbrook. 2087
Email: tbc
Web: www.velqcore.com.au
The cards need to have two different names for the two directors.
Gregory Halvane & Peter Langwade (two separate business cards)

```html
<!DOCTYPE html>
<html lang="en">
<head>
<meta charset="utf-8">
<title>VelqCore Business Card</title>
<link rel="stylesheet" href="https://fonts.googleapis.com/css2?family=Arimo:wght@400;700&display=swap">
<style>
  :root {
    --page-bg: #2b2521;
    --card-blue: #1da1dc;
    --card-blue-deep: #1593cf;
    --text-white: #ffffff;
    --text-dark: #16191c;
    --icon-stroke: #ffffff;
  }
  * { margin: 0; padding: 0; box-sizing: border-box; }
  html, body {
    width: 1200px;
    height: 900px;
    overflow: hidden;
    background: var(--page-bg);
    font-family: "Arimo", Arial, sans-serif;
  }
  .canvas {
    width: 1200px;
    height: 900px;
    display: flex;
    align-items: center;
    justify-content: center;
  }
  .business-card {
    position: relative;
    width: 1000px;
    height: 572px;
    background: radial-gradient(circle at 27% 42%, var(--card-blue) 0%, var(--card-blue-deep) 100%);
    box-shadow: 0 18px 40px rgba(0, 0, 0, 0.45);
    color: var(--text-dark);
  }
  .brand {
    position: absolute;
    left: 120px;
    top: 78px;
    width: 300px;
    display: flex;
    flex-direction: column;
    align-items: center;
  }
  .brand-mark {
    width: 170px;
    height: 170px;
    border-radius: 50%;
    background: var(--text-white);
  }
  .brand-name {
    margin-top: 26px;
    font-size: 58px;
    font-weight: 400;
    color: var(--text-white);
    letter-spacing: 1px;
  }
  .brand-tagline {
    margin-top: 8px;
    font-size: 22px;
    font-weight: 400;
    color: var(--text-dark);
    letter-spacing: 1px;
  }
  .person {
    position: absolute;
    right: 72px;
    top: 148px;
    text-align: right;
  }
  .person-name {
    font-size: 34px;
    font-weight: 700;
    color: var(--text-white);
  }
  .person-role {
    margin-top: 4px;
    font-size: 21px;
    font-weight: 700;
    color: var(--text-dark);
  }
  .contact-list {
    position: absolute;
    left: 520px;
    top: 300px;
    list-style: none;
  }
  .contact-item {
    display: flex;
    align-items: center;
    height: 50px;
    font-size: 23px;
    font-weight: 700;
    white-space: nowrap;
  }
  .contact-icon {
    width: 30px;
    height: 30px;
    margin-right: 18px;
    flex: none;
  }
  .contact-icon * {
    fill: none;
    stroke: var(--icon-stroke);
    stroke-width: 1.8;
    stroke-linecap: round;
    stroke-linejoin: round;
  }
</style>
</head>
<body>
<main class="canvas">
  <article class="business-card">
    <section class="brand">
      <div class="brand-mark"></div>
      <div class="brand-name">VelqCore</div>
      <div class="brand-tagline">Sites Built for Phones</div>
    </section>

    <section class="person">
      <div class="person-name">Peter Langwade</div>
      <div class="person-role">Director</div>
    </section>

    <ul class="contact-list">
      <li class="contact-item">
        <svg class="contact-icon" viewBox="0 0 30 30" aria-hidden="true">
          <path d="M15 27 C9 19 6 15 6 11 A9 9 0 0 1 24 11 C24 15 21 19 15 27 Z"/>
          <circle cx="15" cy="11" r="3.5"/>
        </svg>
        5/41 Dunmore rd, Kelbrook. 2087
      </li>
      <li class="contact-item">
        <svg class="contact-icon" viewBox="0 0 30 30" aria-hidden="true">
          <rect x="9" y="3" width="12" height="24" rx="2"/>
          <line x1="13" y1="23" x2="17" y2="23"/>
          <rect x="11.5" y="6.5" width="7" height="12"/>
        </svg>
        00000 00000
      </li>
      <li class="contact-item">
        <svg class="contact-icon" viewBox="0 0 30 30" aria-hidden="true">
          <rect x="3" y="7" width="24" height="16" rx="1"/>
          <path d="M3 8 L15 17 L27 8"/>
        </svg>
        info@velqcore.com.au
      </li>
      <li class="contact-item">
        <svg class="contact-icon" viewBox="0 0 30 30" aria-hidden="true">
          <circle cx="15" cy="15" r="11"/>
          <ellipse cx="15" cy="15" rx="5" ry="11"/>
          <line x1="4" y1="15" x2="26" y2="15"/>
          <path d="M6 9 H24 M6 21 H24"/>
        </svg>
        www.velqcore.com.au
      </li>
    </ul>
  </article>
</main>
</body>
</html>
```